Dennis K. Halloway stationery and new logo

Create Word template stationery, with a logo, for a Forensic Psychiatry business.

The stationery must include contact info (see below)

The logo should include images similar to (but not necessarily identical to) the ones in the uploaded document. They are the scales of justice and the caduceus, or staff, associated with medicine.

Target Market(s)

consumers of forensic psychiatry (usually lawyers and their clients)

Industry/Entity Type

Mental Health

Logo Text

Dennis K. Halloway, MD, DLFAPA

Font styles to use
Serif

Colors

Designer to choose colors to be used in the design.

Requirements
Must have
• Forensic Psychiatry
• 317 N. Birchwood Lane
• T Building
• East Marlow, PA 19274
• (484) 735-2168
Nice to have
• Conservative color scheme

```html
<!DOCTYPE html>
<html lang="en">
<head>
<meta charset="utf-8">
<title>Dennis K. Halloway — Stationery</title>
<link rel="stylesheet" href="https://fonts.googleapis.com/css2?family=Libre+Caslon+Text:wght@400&family=Lato:wght@400&display=swap">
<style>
  :root {
    --backdrop: #e4e8ea;
    --paper: #ffffff;
    --ink: #1f2a30;
    --text: #3b4247;
    --brand: #0c2a35;
    --brand-light: #ffffff;
  }
  * { margin: 0; padding: 0; box-sizing: border-box; }
  html, body { width: 1200px; height: 910px; overflow: hidden; }
  body {
    background: var(--backdrop);
    font-family: "Lato", Arial, sans-serif;
    position: relative;
  }
  .letterhead {
    position: absolute; left: 153px; top: 184px;
    width: 399px; height: 542px;
    background: var(--paper);
    border-radius: 11px;
    box-shadow: 0 1px 3px rgba(0,0,0,.18);
    color: var(--text);
  }
  .brand-block { position: absolute; left: 44px; top: 36px; display: flex; align-items: center; }
  .brand-dot { width: 30px; height: 30px; border-radius: 50%; background: var(--brand); margin-right: 16px; }
  .brand-name {
    font-family: "Libre Caslon Text", Georgia, serif;
    font-size: 13.6px; color: var(--brand); letter-spacing: .2px; white-space: nowrap;
    line-height: 1;
  }
  .brand-specialty {
    display: flex; align-items: center; gap: 5px; margin-top: 2px;
    font-family: "Libre Caslon Text", Georgia, serif;
    font-size: 6.6px; letter-spacing: 1.6px; color: var(--brand); text-transform: uppercase;
  }
  .brand-specialty::before, .brand-specialty::after { content: ""; flex: 1; height: .8px; background: var(--brand); }
  .brand-address { font-size: 5.6px; color: var(--ink); text-align: center; margin-top: 2px; white-space: nowrap; }
  .letter-body { position: absolute; left: 44px; top: 139px; width: 296px; }
  .salutation { font-size: 9.4px; color: var(--ink); margin-bottom: 22px; }
  .letter-body p.copy {
    font-size: 6.7px; line-height: 10.8px; text-align: justify; margin-bottom: 10px;
  }
  .sign-name { font-size: 9.4px; color: var(--ink); margin-top: 16px; }
  .sign-title { font-size: 6.2px; margin-top: 4px; }
  .signature-area {
    display: block; margin-top: 20px; margin-left: -10px;
    width: 80px; height: 30px; border-radius: 4px;
    background: linear-gradient(90deg, #eef0f1, #f6f7f7);
  }
  .folder { position: absolute; left: 614px; top: 184px; width: 400px; height: 542px; }
  .folder-mark {
    position: absolute; left: 186px; top: 150px; width: 142px;
    display: flex; flex-direction: column; align-items: center; gap: 10px;
  }
  .folder-dot { width: 46px; height: 46px; border-radius: 50%; background: var(--brand-light); }
  .folder-name {
    font-family: "Libre Caslon Text", Georgia, serif;
    font-size: 11px; color: var(--brand-light); text-align: center; line-height: 1.4; letter-spacing: .5px;
  }
</style>
</head>
<body>
  <article class="letterhead">
    <header class="brand-block">
      <div class="brand-dot"></div>
      <div class="brand-text">
        <div class="brand-name">DENNIS K. HALLOWAY, MD, DLFAPA</div>
        <div class="brand-specialty">Forensic Psychiatry</div>
        <div class="brand-address">317 N. Birchwood Lane. T Building. East Marlow, PA 19274. (484) 735-2168</div>
      </div>
    </header>
    <section class="letter-body">
      <p class="salutation">Dear Mr. Carver,</p>
      <p class="copy">Lorem ipsum dolor sit amet, consectetur adipiscing elit. Donec orci purus, luctus vitae dignissim eu, iaculis sed purus. Vivamus faucibus, ipsum nec aliquet viverra, leo mauris condimentum ligula, sit amet sagittis enim ligula quis arcu. Nam egestas tortor id nisi porttitor mattis. In tortor ante, ultricies in suscipit a, tempus non massa. Vivamus et auctor mi. Fusce vel massa nulla. Phasellus nec eros mauris, et scelerisque orci. Donec malesuada orci vitae nulla accumsan porta a id massa. Quisque accumsan iaculis magna sit amet fringilla. Maecenas consequat, magna eget tincidunt semper, odio nibh rutrum mi, id feugiat ante nisi eu risus. Vestibulum nunc orci, rhoncus a placerat in, ultricies in mi. Cras mattis varius eros, vel fringilla nisi suscipit eget.</p>
      <p class="copy">Quisque scelerisque sagittis nulla at porttitor. Mauris a justo et tellus interdum tristique. Sed id augue vitae urna euismod commodo aliquet a quam. Pellentesque arcu velit, cursus et malesuada ut, consequat et diam. Nullam erat sem, rhoncus id ullamcorper vitae, rhoncus et arcu. In ultricies ultricies nulla, ut rutrum nisi iaculis at. Donec eu magna a metus ornare faucibus. Fusce aliquet faucibus ultricies. Morbi semper, est id tincidunt gravida, sem arcu adipiscing lacus, ac bibendum nulla leo eu purus. Quisque nec diam sed risus consectetur a ccumsan quis quis nibh. Vestibulum id purus lorem.</p>
      <p class="sign-name">Alan Mercer</p>
      <p class="sign-title">Co-Founder &amp; CEO</p>
      <span class="signature-area" role="img" aria-label="Handwritten signature of Alan Mercer"></span>
    </section>
  </article>

  <div class="folder">
    <svg width="400" height="542" viewBox="0 0 400 542" aria-hidden="true">
      <defs>
        <linearGradient id="folderFill" x1="0" y1="0" x2="0" y2="1">
          <stop offset="0" stop-color="#0d2d38"/>
          <stop offset="1" stop-color="#0a2630"/>
        </linearGradient>
      </defs>
      <rect x="0" y="0" width="400" height="542" rx="12" fill="url(#folderFill)"/>
      <path d="M400 115 C388 118 385 124 374 130 C370 132 370 136 370 140 L370 238 C370 246 376 252 384 256 L400 262 Z" fill="#082029" opacity=".7"/>
    </svg>
    <div class="folder-mark">
      <div class="folder-dot"></div>
      <div class="folder-name">DENNIS K. HALLOWAY<br>MD, DLFAPA</div>
    </div>
  </div>
</body>
</html>
```